Design Card that Captures Life's Moments

Thinking black and white design with maybe some accent colors. Open to others too. Looking for bold and modern to accompany new logo design. For the side without my info, would have tagline of "Capturing Life's Moments" with either logo or website petravossimaging.com. I want the tagline to dominate and be the main focus of that side.

Target Market(s)

Something that can appeal to people who might be interested in family/kids, business, sports, commercial, or birth/newborn photography.

Industry/Entity Type

Professional Photography

Contact Information for Business Card

Font styles to use
Sans Serif
Script
Other font styles liked:
• Go with Logo, but the tagline could be script that popped.

Requirements
Must have
• See details above! Wow factor! Make someone pick my card up and take it home or at least to look at it further.
• Tagline: Capturing Life's Moments (Main text on side without name)
• INFO:
• Petra Voss-Hale - Photographer
• 555-318-0462 - Cell and for SMS
• www.petravossimaging.com - Website (maybe on side with tagline?)
• petra@petrastudioframes.com - Email
Nice to have
• JUST AN IDEA... I would like to see Capturing Life's Moment really take over most of one side of the card. Think greeting card. Where you can't miss it. It is in your face, but nice and elegant. Maybe cursive, but could work with other font. Instead of logo on tagline side, just have petravossimaging.com in smaller text along one of the edges.
Should not have
• Too simple I could of created it, like with only my logo and some typed text.

```html
<!DOCTYPE html>
<html lang="en">
<head>
<meta charset="utf-8">
<title>Petra Voss-Hale – Business Card</title>
<link rel="stylesheet" href="https://fonts.googleapis.com/css2?family=Cutive+Mono&family=Open+Sans:wght@300;400&family=Sacramento&display=swap">
<style>
  :root {
    --canvas: #ffffff;
    --front-dark: #0b0c0c;
    --front-mid: #2c3030;
    --front-text: #f2f2f2;
    --back-paper: #ffffff;
    --back-border: #9a9a9a;
    --back-ink: #1b1b1b;
    --shutter-light: #d9d9d9;
    --shutter-mid: #b5b5b5;
  }
  html, body {
    margin: 0;
    padding: 0;
    width: 1200px;
    height: 360px;
    overflow: hidden;
    background: var(--canvas);
  }
  .card-sheet {
    position: relative;
    width: 1200px;
    height: 360px;
  }
  .card {
    position: absolute;
    top: 0;
    height: 358px;
    overflow: hidden;
    box-sizing: border-box;
  }
  /* Front side */
  .card-front {
    left: 0;
    width: 598px;
    background: radial-gradient(ellipse 420px 300px at 180px 220px, var(--front-mid) 0%, #15181a 60%, var(--front-dark) 100%);
    color: var(--front-text);
    font-family: "Open Sans", sans-serif;
  }
  .front-decor {
    position: absolute;
    inset: 0;
  }
  .brand-name {
    position: absolute;
    left: 40px;
    top: 48px;
    margin: 0;
    font-family: "Open Sans", sans-serif;
    font-weight: 300;
    font-size: 26px;
    letter-spacing: 2px;
    color: var(--front-text);
  }
  .person {
    position: absolute;
    right: 38px;
    top: 148px;
    text-align: right;
  }
  .person-name {
    margin: 0;
    font-family: "Cutive Mono", monospace;
    font-size: 28px;
    letter-spacing: 1px;
    line-height: 1.1;
  }
  .person-role {
    margin: 10px 0 0;
    font-weight: 300;
    font-size: 16px;
    letter-spacing: 0.5px;
  }
  .contact {
    position: absolute;
    right: 38px;
    top: 282px;
    text-align: right;
    font-weight: 300;
    line-height: 1.45;
  }
  .contact-phone { margin: 0; font-size: 17px; }
  .contact-email { margin: 0; font-size: 15px; }

  /* Back side */
  .card-back {
    left: 600px;
    width: 600px;
    background: var(--back-paper);
    border: 1px solid var(--back-border);
    color: var(--back-ink);
  }
  .back-decor {
    position: absolute;
    left: 0;
    top: 0;
  }
  .tagline {
    position: absolute;
    left: 0;
    right: 0;
    top: 148px;
    margin: 0;
    padding-left: 10px;
    text-align: center;
    font-family: "Sacramento", cursive;
    font-weight: 400;
    font-size: 46px;
    letter-spacing: 1px;
  }
  .website {
    position: absolute;
    left: 0;
    right: 0;
    top: 306px;
    margin: 0;
    text-align: center;
    font-family: "Open Sans", sans-serif;
    font-size: 17px;
    letter-spacing: 0.3px;
  }
</style>
</head>
<body>
<main class="card-sheet">
  <section class="card card-front" aria-label="Card front">
    <svg class="front-decor" width="598" height="358" viewBox="0 0 598 358" role="img" aria-label="Large dark camera shutter aperture decoration">
      <defs>
        <radialGradient id="shutterGlow" cx="0.5" cy="0.5" r="0.5">
          <stop offset="0" stop-color="#1c1f20"/>
          <stop offset="0.7" stop-color="#111314"/>
          <stop offset="1" stop-color="#0a0b0b" stop-opacity="0"/>
        </radialGradient>
      </defs>
      <circle cx="95" cy="90" r="215" fill="url(#shutterGlow)"/>
      <circle cx="610" cy="345" r="95" fill="url(#shutterGlow)"/>
    </svg>
    <p class="brand-name">Petra Voss Imaging</p>
    <div class="person">
      <h1 class="person-name">Petra Voss-Hale</h1>
      <p class="person-role">PHOTOGRAPHER</p>
    </div>
    <div class="contact">
      <p class="contact-phone">555-318-0462</p>
      <p class="contact-email">petra@petrastudioframes.com</p>
    </div>
  </section>

  <section class="card card-back" aria-label="Card back">
    <svg class="back-decor" width="250" height="230" viewBox="0 0 250 230" role="img" aria-label="Soft grey camera shutter aperture decoration">
      <defs>
        <linearGradient id="shutterGrey" x1="0" y1="0" x2="1" y2="1">
          <stop offset="0" stop-color="#ededed"/>
          <stop offset="1" stop-color="#bdbdbd"/>
        </linearGradient>
      </defs>
      <path d="M0 0 H250 A250 225 0 0 1 0 225 Z M0 0 H190 A190 175 0 0 1 0 175 Z" fill="url(#shutterGrey)" fill-rule="evenodd"/>
    </svg>
    <h2 class="tagline">Capturing Life’s Moment</h2>
    <p class="website">www.petravossimaging.com</p>
  </section>
</main>
</body>
</html>
```